Daxholm APP redesign and color change

I am looking for a new design for my app. Please see the attached current design.

Currently, I have a functioning app but the colors and design are awful!
The logo is great but the rest of the app needs a refresh.
(Logo hi res not yet available but will upload soon.)
New colors or anything that is cutting edge.

Basically: It is a secure social media app within a school system where the teachers, students and parents can text, exchange photos, plan curriculum, etc.

I NEED ONLY landing page with a new look!
Looking for one distinct design for the landing page with new look.
The developer will apply this one design towards the rest of the pages/app screens.

Because part of the social media I need the feel and look of what is now the trend. Something that will attract and keep the client(s) interested. I am really leaving all the creative work to the designer and open to any suggestions.
Updates

Target Market(s)

Schools, community, teachers, students, colleges, sport teams

Industry/Entity Type

Non Profit

Font styles to use
Serif
Sans Serif

Colors

Designer to choose colors to be used in the design.

Requirements
Must have
• Sharp, trendy, millennial feel
Nice to have
• Up to designer
Should not have
• Up to designer

```html
<!DOCTYPE html>
<html lang="en">
<head>
<meta charset="utf-8">
<title>Daxholm – Messaging Screens</title>
<link rel="stylesheet" href="https://fonts.googleapis.com/css2?family=Fira+Sans:ital,wght@0,300;0,400;0,500;1,300;1,400&display=swap">
<style>
:root{
  --stage:#4a4a4a;
  --brand-start:#ee3a5a;
  --brand-end:#e3198f;
  --brand-mid:#ea2a74;
  --tab-active:#c92348;
  --ink:#353535;
  --muted:#8b8b8b;
  --divider:#e6e6e6;
  --chat-bg:#efefef;
  --white:#ffffff;
  --soft-btn:#ef6a7c;
}
*{box-sizing:border-box;margin:0;padding:0}
html,body{width:1200px;height:800px;overflow:hidden;background:var(--stage);font-family:"Fira Sans",sans-serif}
.screen{position:absolute;top:33px;width:414px;height:733px;background:var(--white);overflow:hidden;box-shadow:0 10px 30px rgba(0,0,0,.35)}
.screen--inbox{left:152px}
.screen--chat{left:620px;background:var(--chat-bg)}
.topbar{position:absolute;left:0;top:0;width:100%;background:linear-gradient(90deg,var(--brand-start),var(--brand-end));color:var(--white)}
.screen--inbox .topbar{height:87px}
.screen--chat .topbar{height:89px}
.status{position:absolute;top:6px;left:8px;right:8px;height:14px;font-size:12.5px;display:flex;justify-content:space-between;align-items:center}
.status .time{position:absolute;left:50%;transform:translateX(-50%)}
.status .right{display:flex;align-items:center;gap:5px}
.battery{width:26px;height:11px;border:1px solid var(--white);border-radius:2px;position:relative}
.battery::before{content:"";position:absolute;left:1px;top:1px;width:5px;height:7px;background:var(--white)}
.nav-back{position:absolute;left:16px;top:45px;display:flex;align-items:center;gap:8px;font-size:17px;font-style:italic;font-weight:300}
.brand-name{position:absolute;left:50%;top:44px;transform:translateX(-50%);font-size:20px;font-weight:400;letter-spacing:.3px}
.head-icons{position:absolute;right:18px;top:44px;display:flex;gap:18px}
.chat-title{position:absolute;left:16px;top:45px;display:flex;align-items:center;gap:14px;font-size:24px;font-style:italic;font-weight:400}
.search-row{position:absolute;top:87px;left:0;width:100%;height:47px;display:flex;align-items:center;padding-left:22px;gap:20px;color:var(--muted);font-size:16px;font-weight:300;box-shadow:0 3px 6px rgba(0,0,0,.06);background:var(--white)}
.contacts{position:absolute;top:141px;left:0;width:100%;list-style:none}
.contact{position:relative;height:93px;border-bottom:1px solid var(--divider);margin-left:22px}
.avatar{position:absolute;border-radius:50%}
.contact .avatar{left:0;top:16px;width:59px;height:59px}
.contact .name{position:absolute;left:75px;top:22px;font-size:17px;font-weight:500;color:var(--ink)}
.contact .preview{position:absolute;left:75px;top:48px;font-size:14.5px;font-weight:300;color:var(--muted)}
.open-chat{position:absolute;right:17px;top:29px;width:34px;height:34px;border-radius:50%;background:linear-gradient(135deg,var(--brand-start),var(--brand-end));display:flex;align-items:center;justify-content:center}
.tabbar{position:absolute;bottom:0;left:0;width:100%;height:55px;background:linear-gradient(90deg,var(--brand-start),var(--brand-end));display:flex}
.tab{flex:1;display:flex;align-items:center;justify-content:center}
.tab--active{background:var(--tab-active)}
.stamp{position:absolute;top:110px;width:100%;text-align:center;font-size:13px;color:var(--brand-start)}
.msg{position:absolute;height:40px;display:flex;align-items:center;padding:0 16px;font-size:14.5px;font-weight:400}
.msg--in{left:65px;background:linear-gradient(90deg,var(--brand-start),var(--brand-end));color:var(--white)}
.msg--out{background:var(--white);color:var(--ink)}
.chat-avatar{width:34px;height:34px}
.video{position:absolute;left:65px;top:330px;width:313px;height:210px;background:var(--white);box-shadow:0 2px 6px rgba(0,0,0,.08)}
.video .frame{position:absolute;left:0;top:0;width:100%;height:172px;background:linear-gradient(100deg,#d6d8da 0%,#cfd2d4 40%,#b9b3b0 70%,#d4d6d8 100%)}
.play{position:absolute;left:139px;top:88px;width:34px;height:34px;border-radius:50%;background:var(--brand-end);display:flex;align-items:center;justify-content:center}
.track{position:absolute;left:16px;top:191px;width:280px;height:2px;background:#cfcfcf}
.track .buffer{position:absolute;left:0;top:0;width:157px;height:2px;background:#f6a2a8}
.track .played{position:absolute;left:0;top:0;width:116px;height:2px;background:var(--brand-start)}
.track .knob{position:absolute;left:109px;top:-6px;width:14px;height:14px;border-radius:50%;background:var(--brand-start)}
.composer{position:absolute;bottom:0;left:0;width:100%;height:72px;background:var(--white);display:flex;align-items:center;padding-left:22px}
.composer .hint{font-size:16.5px;font-style:italic;font-weight:300;color:#777}
.composer .actions{position:absolute;right:12px;top:18px;display:flex;gap:12px}
.round{width:38px;height:38px;border-radius:50%;background:var(--soft-btn);display:flex;align-items:center;justify-content:center}
.round--send{background:var(--brand-end)}
</style>
</head>
<body>

<section class="screen screen--inbox">
  <header class="topbar">
    <div class="status">
      <span>●●●○○ NOVA</span><span class="time">4:21 PM</span>
      <span class="right">22% <span class="battery"></span></span>
    </div>
    <div class="nav-back">
      <svg width="14" height="22" viewBox="0 0 14 22"><path d="M12 2 3 11l9 9" fill="none" stroke="#fff" stroke-width="2.5"/></svg>Back
    </div>
    <div class="brand-name">Daxholm</div>
    <div class="head-icons">
      <svg width="24" height="24" viewBox="0 0 24 24"><circle cx="12" cy="12" r="11" fill="#fff"/><path d="M6 6c3 1 2 4 5 5s1 5 3 7M16 3c-1 3 2 4 4 5" fill="none" stroke="#ea2a74" stroke-width="2.2"/></svg>
      <svg width="24" height="24" viewBox="0 0 24 24"><circle cx="10" cy="10" r="7.5" fill="none" stroke="#fff" stroke-width="2.5"/><path d="M15.5 15.5 22 22" stroke="#fff" stroke-width="2.8"/></svg>
    </div>
  </header>

  <div class="search-row">
    <svg width="20" height="20" viewBox="0 0 24 24"><circle cx="10" cy="10" r="7.5" fill="none" stroke="#ee3a5a" stroke-width="2.5"/><path d="M15.5 15.5 22 22" stroke="#ee3a5a" stroke-width="2.8"/></svg>
    <span>Search Conversations...</span>
  </div>

  <ul class="contacts">
    <li class="contact"><div class="avatar" role="img" aria-label="Profile photo of Marisa Holt" style="background:#6b5a52"></div><span class="name">Marisa Holt</span><span class="preview">Hlo How Are You ?</span><span class="open-chat"><svg width="16" height="16" viewBox="0 0 16 16"><path d="M8 2a6 5.5 0 1 1-3 10.3L2 14l1-3A5.5 5.5 0 0 1 8 2z" fill="#fff"/></svg></span></li>
    <li class="contact"><div class="avatar" role="img" aria-label="Profile photo of Tobias Rennick" style="background:#a98f7c"></div><span class="name">Tobias Rennick</span><span class="preview">Tonight I am Going Home</span><span class="open-chat"><svg width="16" height="16" viewBox="0 0 16 16"><path d="M8 2a6 5.5 0 1 1-3 10.3L2 14l1-3A5.5 5.5 0 0 1 8 2z" fill="#fff"/></svg></span></li>
    <li class="contact"><div class="avatar" role="img" aria-label="Profile photo of Owen Castell" style="background:#5d5855"></div><span class="name">Owen Castell</span><span class="preview">So Whats Going on There</span><span class="open-chat"><svg width="16" height="16" viewBox="0 0 16 16"><path d="M8 2a6 5.5 0 1 1-3 10.3L2 14l1-3A5.5 5.5 0 0 1 8 2z" fill="#fff"/></svg></span></li>
    <li class="contact"><div class="avatar" role="img" aria-label="Profile photo of Vera Lindqvist" style="background:#2f4a52"></div><span class="name">Vera Lindqvist</span><span class="preview">Hlo All Things is Working</span><span class="open-chat"><svg width="16" height="16" viewBox="0 0 16 16"><path d="M8 2a6 5.5 0 1 1-3 10.3L2 14l1-3A5.5 5.5 0 0 1 8 2z" fill="#fff"/></svg></span></li>
    <li class="contact"><div class="avatar" role="img" aria-label="Profile photo of Dorian Blake" style="background:#b0846a"></div><span class="name">Dorian Blake</span><span class="preview">Amazing App Design</span><span class="open-chat"><svg width="16" height="16" viewBox="0 0 16 16"><path d="M8 2a6 5.5 0 1 1-3 10.3L2 14l1-3A5.5 5.5 0 0 1 8 2z" fill="#fff"/></svg></span></li>
    <li class="contact"><div class="avatar" role="img" aria-label="Profile photo of Celia Marsh" style="background:#7d8a5a"></div><span class="name">Celia Marsh</span><span class="preview">This Gona Be Rock</span><span class="open-chat"><svg width="16" height="16" viewBox="0 0 16 16"><path d="M8 2a6 5.5 0 1 1-3 10.3L2 14l1-3A5.5 5.5 0 0 1 8 2z" fill="#fff"/></svg></span></li>
  </ul>

  <nav class="tabbar">
    <div class="tab tab--active"><svg width="34" height="28" viewBox="0 0 34 28" fill="none" stroke="#fff" stroke-width="1.6"><path d="M2 2h22v14H10l-5 4v-4H2z"/><path d="M12 19v3h14l5 4v-4h1V8h-6"/><path d="M6 7h14M6 11h10"/></svg></div>
    <div class="tab"><svg width="28" height="28" viewBox="0 0 28 28" fill="none" stroke="#fff" stroke-width="2"><rect x="2" y="2" width="10" height="10" rx="2"/><rect x="16" y="2" width="10" height="10" rx="2"/><rect x="2" y="16" width="10" height="10" rx="2"/><rect x="16" y="16" width="10" height="10" rx="2"/></svg></div>
    <div class="tab"><svg width="28" height="30" viewBox="0 0 28 30" fill="none" stroke="#fff" stroke-width="1.6"><rect x="3" y="2" width="22" height="26" rx="1"/><path d="M1 8h4M1 15h4M1 22h4M22 2v26"/><circle cx="13" cy="13" r="4"/><path d="M7 22c1-4 11-4 12 0"/></svg></div>
    <div class="tab"><svg width="28" height="28" viewBox="0 0 28 28" fill="none" stroke="#fff" stroke-width="1.6"><circle cx="11" cy="11" r="3"/><path d="M11 2v3M11 17v3M2 11h3M17 11h3M4.6 4.6l2 2M15.4 15.4l2 2M4.6 17.4l2-2M15.4 6.6l2-2"/><circle cx="11" cy="11" r="6"/><circle cx="21" cy="21" r="4"/><circle cx="21" cy="21" r="1.5"/></svg></div>
  </nav>
</section>

<section class="screen screen--chat">
  <header class="topbar">
    <div class="status">
      <span>●●●○○ NOVA</span><span class="time">4:21 PM</span>
      <span class="right">22% <span class="battery"></span></span>
    </div>
    <div class="chat-title">
      <svg width="14" height="24" viewBox="0 0 14 24"><path d="M12 2 3 12l9 10" fill="none" stroke="#fff" stroke-width="2.5"/></svg>Marisa Holt
    </div>
  </header>

  <div class="stamp">9:20 PM</div>

  <div class="avatar chat-avatar" role="img" aria-label="Profile photo of Marisa Holt" style="left:15px;top:149px;background:#6b5a52"></div>
  <div class="msg msg--in" style="top:145px">Hlo How Are You ?</div>

  <div class="msg msg--out" style="left:190px;top:209px;width:179px">I ‘m Fine You Say Dear</div>
  <div class="avatar chat-avatar" role="img" aria-label="Profile photo of the user" style="left:373px;top:213px;background:#8f8c88"></div>

  <div class="avatar chat-avatar" role="img" aria-label="Profile photo of Marisa Holt" style="left:15px;top:277px;background:#6b5a52"></div>
  <div class="msg msg--in" style="top:274px">Please send me video :D</div>

  <div class="video">
    <div class="frame" role="img" aria-label="Video thumbnail: fashion portrait with bold eye makeup"></div>
    <div class="play"><svg width="12" height="14" viewBox="0 0 12 14"><path d="M2 1l9 6-9 6z" fill="#fff"/></svg></div>
    <div class="track"><span class="buffer"></span><span class="played"></span><span class="knob"></span></div>
  </div>

  <footer class="composer">
    <span class="hint">Type here...</span>
    <div class="actions">
      <span class="round"><svg width="16" height="14" viewBox="0 0 16 14" fill="none" stroke="#fff" stroke-width="1.6"><rect x="1" y="1" width="14" height="12"/><path d="M3 11l4-4 3 3 2-2 2 3"/><circle cx="11" cy="4.5" r="1.2" fill="#fff"/></svg></span>
      <span class="round"><svg width="18" height="12" viewBox="0 0 18 12"><rect x="0" y="1" width="12" height="10" rx="1" fill="#fff"/><path d="M12 6l6-4v8z" fill="#fff"/></svg></span>
      <span class="round round--send"><svg width="18" height="18" viewBox="0 0 18 18"><path d="M1 8 17 1l-6 16-3-6z" fill="#fff"/><path d="M8 11l9-10" stroke="#e3198f" stroke-width="1.2"/></svg></span>
    </div>
  </footer>
</section>

</body>
</html>
```